I am a company selling interior designing materials

HI, I am selling interior design materials and require a namecard which is more outstanding while following a certain details placement as attached.

My clients are mainly interior designers so it has to attract their attention rather than feeling that its "just another namecard". I am selling wallcoverings, fabrics, acoustics and carpets.

Target Market(s)

interior designers designing hotels, commerical offices.

Contact Information for Business Card

As per attached.
Please change address to 47 Jalan 16 Tampines #05-02 Velmora Building Singapore 527314

Font styles to use
Other font styles liked:
• calibri

Requirements
Must have
• (1) company logo on top in the middle. Placement of contac details to be the same
• (2) company color is blue/green cymk 75/8/42/0
• (3) "KTV" logo to be prominent
• (4) You may change the logo but there should be a "swirl" surrounding the word KTV like current logo. The swirl pattern does not need to follow current logo and you may propose.
Should not have
• (1) there should not be any designs above "KTV" logo
• (2) no sharp triangles or angles

```html
<!DOCTYPE html>
<html lang="en">
<head>
<meta charset="utf-8">
<title>KTV Interior Furnishings – Business Card</title>
<link rel="stylesheet" href="https://fonts.googleapis.com/css2?family=Carlito:wght@400;700&display=swap">
<style>
  :root {
    --stage: #2b2b2d;
    --ink: #0d0d0d;
    --paper: #ffffff;
    --accent-red: #e8323a;
    --brand-teal: #3fb3a0;
    --text-grey: #6e6e6e;
    --text-light: #f2f2f2;
  }
  * { margin: 0; padding: 0; box-sizing: border-box; }
  html, body {
    width: 1200px; height: 896px; overflow: hidden;
    background: var(--stage);
    font-family: "Carlito", "Calibri", sans-serif;
  }
  .stage { position: relative; width: 1200px; height: 896px; }
  .card {
    position: absolute; width: 540px; height: 309px;
    border-radius: 22px; overflow: hidden;
  }
  /* Back of card */
  .card-back {
    left: 120px; top: 90px;
    background: var(--ink);
    color: var(--text-light);
    display: flex; flex-direction: column; align-items: center; justify-content: center;
  }
  .brand { display: flex; align-items: center; gap: 12px; }
  .brand-dot {
    width: 18px; height: 18px; border-radius: 50%;
    background: var(--brand-teal);
  }
  .brand-name { font-weight: 700; font-size: 62px; letter-spacing: 2px; line-height: 1; }
  .card-back .brand-name { color: var(--paper); }
  .company-name { font-weight: 700; font-size: 19px; margin-top: 16px; }
  .services { font-size: 16px; letter-spacing: 1.5px; margin-top: 30px; }
  /* Front of card */
  .card-front {
    left: 540px; top: 497px;
    background: var(--paper);
  }
  .wave { position: absolute; inset: 0; width: 540px; height: 309px; }
  .front-brand {
    position: absolute; left: 30px; top: 92px;
    display: flex; flex-direction: column; align-items: center;
  }
  .card-front .brand-name { color: var(--text-grey); font-size: 54px; }
  .card-front .company-name { color: var(--text-grey); font-size: 15px; margin-top: 12px; }
  .contact {
    position: absolute; right: 24px; top: 42px;
    text-align: right; color: var(--text-light);
    font-size: 13.5px; line-height: 1.5;
  }
  .contact-name {
    color: var(--accent-red); font-weight: 700; font-size: 23px;
    letter-spacing: 0.5px; margin-bottom: 8px;
  }
  .contact-line { display: flex; justify-content: flex-end; align-items: center; gap: 8px; }
  .contact-line svg { width: 12px; height: 12px; flex: none; }
  .contact-address { margin-top: 12px; }
</style>
</head>
<body>
<main class="stage">
  <section class="card card-back">
    <div class="brand">
      <span class="brand-dot"></span>
      <span class="brand-name">KTV</span>
    </div>
    <p class="company-name">KeTavio Interior Furnishings Pte Ltd</p>
    <p class="services">WALLCOVERINGS - ACOUSTIC - FABRICS - CARPET</p>
  </section>

  <section class="card card-front">
    <svg class="wave" viewBox="0 0 540 309" aria-hidden="true">
      <path d="M135 309 C225 296 268 245 276 175 C278 150 280 138 283 128 C286 175 280 255 180 309 Z" fill="var(--accent-red)"/>
      <path d="M370 0 H540 V309 H215 C262 290 286 248 290 195 C296 105 318 35 370 0 Z" fill="var(--ink)"/>
    </svg>

    <div class="front-brand">
      <div class="brand">
        <span class="brand-dot"></span>
        <span class="brand-name">KTV</span>
      </div>
      <p class="company-name">KeTavio Interior Furnishings Pte Ltd</p>
    </div>

    <div class="contact">
      <p class="contact-name">DELIA TAN</p>
      <p class="contact-line">(65) 6271 4085
        <svg viewBox="0 0 12 12"><path d="M3 1 L5 3.5 L4 5 C5 7 6 8 7.5 8.5 L9 7.5 L11 9.5 L9.5 11 C5 10.5 1.5 7 1 2.5 Z" fill="var(--accent-red)"/></svg>
      </p>
      <p class="contact-line">(65) 9315 7724
        <svg viewBox="0 0 12 12"><rect x="3" y="0.8" width="6" height="10.4" rx="1.2" fill="none" stroke="var(--accent-red)" stroke-width="1.3"/></svg>
      </p>
      <p class="contact-line">delia@ktvfurnishings.com
        <svg viewBox="0 0 12 12"><rect x="1" y="2.5" width="10" height="7" rx="1" fill="none" stroke="var(--accent-red)" stroke-width="1.2"/><path d="M1.5 3 L6 6.5 L10.5 3" fill="none" stroke="var(--accent-red)" stroke-width="1.2"/></svg>
      </p>
      <p class="contact-address">47 Jalan 16 Tampines #05-02<br>Velmora Building Singapore 527314</p>
    </div>
  </section>
</main>
</body>
</html>
```